Kelvor Datawise Solutions

We need a Logo and Website for our company based in London. We are a IT recruitment company . We provide quality resources to top IT company across UK.

Industry/Entity Type

It Company

Number of Pages Required

4 page

```html
<!DOCTYPE html>
<html lang="en">
<head>
<meta charset="utf-8">
<title>Kelvor Datawise Solutions</title>
<link href="https://fonts.googleapis.com/css2?family=Oswald:wght@300;400;500;600&family=Open+Sans:ital,wght@0,400;0,600;1,400&display=swap" rel="stylesheet">
<style>
:root{
  --orange:#f47a20;
  --orange-soft:#f08b4a;
  --teal:#3cc8c8;
  --green:#6aac45;
  --ink:#444;
  --muted:#777;
  --band:#eeeeee;
  --dark:#2f2f31;
  --white:#fff;
}
*{margin:0;padding:0;box-sizing:border-box}
html,body{width:1200px;height:2233px;overflow:hidden}
body{position:relative;background:var(--white);font-family:"Open Sans",Arial,sans-serif;color:var(--ink)}
.abs{position:absolute}

/* header */
.site-header{left:0;top:0;width:1200px;height:93px;background:var(--white)}
.brand{left:48px;top:30px;display:flex;align-items:center;gap:10px;font-family:"Open Sans",sans-serif;font-size:22px;font-weight:600;color:var(--orange);letter-spacing:.3px}
.brand-mark{width:22px;height:22px;background:var(--orange)}
.main-nav{left:540px;top:0;width:612px;height:93px;display:flex;justify-content:space-between;align-items:center;padding-left:0}
.main-nav a{font-size:11.5px;color:#555;text-decoration:none;text-transform:uppercase;letter-spacing:.2px}
.main-nav a.active{color:var(--orange)}

/* hero */
.hero{left:0;top:93px;width:1200px;height:530px;background:linear-gradient(110deg,#4a4340 0%,#6b625d 35%,#5a5654 65%,#3f3c3b 100%)}
.hero-title{right:53px;top:178px;text-align:right;font-family:"Oswald",sans-serif;color:var(--white);text-transform:uppercase;line-height:1.22}
.hero-title .light{display:block;font-weight:300;font-size:46px}
.hero-title .bold{display:block;font-weight:600;font-size:46px}
.hero-dots{left:1080px;top:478px;display:flex;gap:7px}
.hero-dots span{width:16px;height:16px;border-radius:50%;border:2px solid var(--white)}
.hero-dots span.on{background:var(--orange);border-color:var(--orange)}

/* welcome */
.welcome-rule{left:46px;top:685px;width:1106px;height:1px;background:#ddd}
.welcome-title{left:0;top:662px;width:1200px;text-align:center;font-family:"Oswald",sans-serif;font-weight:500;font-size:30px;color:#444;text-transform:uppercase}
.welcome-title span.wrap{background:var(--white);padding:0 14px}
.welcome-title em{font-style:normal;color:var(--orange)}
.welcome-text{left:100px;top:736px;width:1000px;text-align:center;font-size:12px;line-height:21px;color:#777}
.btn-read{left:528px;top:817px;width:143px;height:47px;background:var(--orange);color:var(--white);font-size:11.5px;text-transform:uppercase;display:flex;align-items:center;justify-content:center}

/* service cards */
.card{top:952px;width:262px;height:318px;display:flex;align-items:center;justify-content:center;font-family:"Oswald",sans-serif;font-size:21px;color:var(--white)}
.card-1{left:47px;background:linear-gradient(135deg,#f29a5e,#ec8443)}
.card-2{left:328px;background:linear-gradient(160deg,#c9b7a4,#8a7b70 60%,#6e6661)}
.card-3{left:610px;background:linear-gradient(135deg,#4fd0cf,#36c3c3)}
.card-4{left:890px;background:linear-gradient(135deg,#74b450,#64a63f)}
.card-bar{left:0;bottom:0;width:262px;height:37px;background:#555;display:flex;align-items:center;justify-content:center;gap:14px;font-size:18px;font-family:"Oswald",sans-serif;letter-spacing:.5px}

/* testimonial */
.testimonial{left:0;top:1324px;width:1200px;height:304px;background:var(--band)}
.quote-box{left:343px;top:1374px;width:398px;height:170px;background:var(--white)}
.quote-text{left:365px;top:1414px;width:358px;font-size:11.5px;font-style:italic;line-height:22px;color:#999}
.avatar{left:765px;top:1354px;width:76px;height:76px;border-radius:50%;background:linear-gradient(160deg,#d8b79d,#3a3a3a)}
.person{left:740px;top:1462px;width:126px;text-align:center}
.person-name{font-size:20px;font-weight:600;color:#555}
.person-place{font-size:11px;color:#888;margin-top:0}

/* get started */
.footer-main{left:0;top:1628px;width:1200px;height:529px;background:linear-gradient(100deg,#3a3a3c 0%,#4a4847 45%,#2c2c2e 100%)}
.gs-title{left:76px;top:1724px;font-size:28px;color:var(--teal);letter-spacing:.3px}
.gs-text{left:76px;top:1776px;width:490px;font-size:12.5px;line-height:21px;color:var(--white)}
.gs-rule{left:76px;top:1855px;width:488px;height:1px;background:#ddd}
.contact-list{left:80px;top:1880px;font-size:15px;line-height:28.5px;color:var(--white);list-style:none}
.field{left:655px;width:488px;border:1px solid #bbb;background:rgba(255,255,255,.07);color:var(--white);font-size:14px;font-weight:600;padding:7px 13px}
.btn-send{left:1007px;top:2077px;width:136px;height:40px;background:var(--white);color:var(--orange);font-size:18px;display:flex;align-items:center;justify-content:center;letter-spacing:1px}

/* bottom bar */
.bottom-bar{left:0;top:2157px;width:1200px;height:76px;background:var(--orange)}
.copyright{left:52px;top:2184px;font-size:10px;color:var(--white)}
.social{left:1002px;top:2173px;display:flex;gap:10px}
.social span{width:28px;height:28px;border:1.5px solid var(--white)}
</style>
</head>
<body>

<header class="site-header abs">
  <div class="brand abs"><span class="brand-mark"></span>Kelvor Datawise Solutions</div>
  <nav class="main-nav abs">
    <a class="active">Home</a><a>About Us</a><a>Our Service</a><a>Project</a><a>Blogs</a><a>Contact Us</a>
  </nav>
</header>

<section class="hero abs" role="img" aria-label="Photo of a team working together at laptops in an office"></section>
<h1 class="hero-title abs"><span class="light">Duis aute irure dolor in reprehenderit</span><span class="bold">Voluptate velit esse cillum dolore</span></h1>
<div class="hero-dots abs"><span class="on"></span><span></span><span></span></div>

<div class="welcome-rule abs"></div>
<h2 class="welcome-title abs"><span class="wrap">Welcome to <em>Kelvor Datawise Solutions</em></span></h2>
<p class="welcome-text abs">Lorem ipsum dolor sit amet, consectetur adipiscing elit, sed do eiusmod tempor incididunt ut labore et dolore magna aliqua. Ut enim ad minim veniam, quis nostrud exercitation ullamco laboris nisi ut aliquip ex ea commodo consequat. Duis aute irure dolor in reprehenderit in voluptate velit esse cillum dolore eu fugiat nulla pariatur. Excepteur sint occaecat cupidatat non proident, sunt in culpa qui officia deserunt mollit anim id est laborum.</p>
<div class="btn-read abs">Read More</div>

<div class="card card-1 abs" role="img" aria-label="Orange-tinted photo of a person reviewing charts on a laptop">Lorem ipsum dolors</div>
<div class="card card-2 abs" role="img" aria-label="Photo of young colleagues working together at a desk">
  <div class="card-bar abs">READ MORE
    <svg width="20" height="20" viewBox="0 0 20 20"><circle cx="10" cy="10" r="8.5" fill="none" stroke="#fff" stroke-width="1.5"/><path d="M8.5 6.5 12 10l-3.5 3.5" fill="none" stroke="#fff" stroke-width="1.8"/></svg>
  </div>
</div>
<div class="card card-3 abs" role="img" aria-label="Teal-tinted photo of a person on the phone">Lorem ipsum dolors</div>
<div class="card card-4 abs" role="img" aria-label="Green-tinted photo of an office workspace">Lorem ipsum dolors</div>

<section class="testimonial abs"></section>
<svg class="abs" style="left:175px;top:1405px" width="40" height="108" viewBox="0 0 40 108"><path d="M38 1 2 54l36 53" fill="none" stroke="#aaa" stroke-width="1.5"/></svg>
<svg class="abs" style="left:981px;top:1405px" width="40" height="108" viewBox="0 0 40 108"><path d="M2 1l36 53L2 107" fill="none" stroke="#aaa" stroke-width="1.5"/></svg>
<div class="quote-box abs"></div>
<svg class="abs" style="left:741px;top:1400px" width="24" height="30" viewBox="0 0 24 30"><path d="M0 0 24 10 0 30z" fill="#fff"/></svg>
<svg class="abs" style="left:336px;top:1362px" width="44" height="34" viewBox="0 0 44 34"><g fill="#bbb"><circle cx="10" cy="22" r="9"/><path d="M2 21Q3 5 16 1l1 3Q8 8 8 18z"/><circle cx="32" cy="22" r="9"/><path d="M24 21Q25 5 38 1l1 3Q30 8 30 18z"/></g></svg>
<p class="quote-text abs">Lorem ipsum dolor sit amet, consectetur adipiscing elit, sed do eiusmod tempor incididunt ut labore et dolore magna aliqua. Ut enim ad minim veniam, quis nostrud exercitation ullamco laboris nisi ut aliquip ex ea commodo consequat.</p>
<div class="avatar abs" role="img" aria-label="Portrait photo of the client"></div>
<div class="person abs"><div class="person-name">Aled Brennan</div><div class="person-place">City &nbsp;Location</div></div>

<section class="footer-main abs" role="img" aria-label="Dark photo of a hand using a device"></section>
<h3 class="gs-title abs">GET STARTED</h3>
<p class="gs-text abs">Lorem ipsum dolor sit amet, consectetur adipiscing elit, sed do eiusmod tempor incididunt ut labore et dolore magna aliqua. Ut enim ad minim veniam, quis nostrud exercitation ullamco laboris nisi ut aliquip ex ea commodo consequat.</p>
<div class="gs-rule abs"></div>
<ul class="contact-list abs">
  <li>123 Address line1, Address line 2</li>
  <li>Country, 123456.</li>
  <li>Freephone: +44 20 7946 0318</li>
  <li>Telephone: +44 20 7946 0318</li>
  <li>FAX: +44 20 7946 0722</li>
  <li>&nbsp;</li>
  <li>E-mail: hello@kelvordatawise.example</li>
</ul>
<div class="field abs" style="top:1780px;height:35px">Name</div>
<div class="field abs" style="top:1847px;height:35px">Email id</div>
<div class="field abs" style="top:1913px;height:35px">Phone</div>
<div class="field abs" style="top:1973px;height:85px">Address</div>
<div class="btn-send abs">SEND</div>

<footer class="bottom-bar abs"></footer>
<p class="copyright abs">Copyright 2016 Company Name. All Rights Reserved.</p>
<div class="social abs"><span></span><span></span><span></span><span></span></div>

</body>
</html>
```